Rise As Captain Book Cover Design

Book Cover Design Brief
Book Title
Rise As Captain
Subtitle
The 10 Quiet Habits of Remarkable Command
Author
Orwen Dalquist
Overview
This book is about leadership that starts within.
Most leadership books focus on tactics or management strategies. This book focuses on the inner disciplines that create powerful leaders — mindset, integrity, focus, empathy, professionalism, honesty, and self-respect.
The tone of the book is bold, direct, confident, and transformational.
This is not a soft or corporate leadership book. It is a call to step up and become the leader you are capable of becoming.
The cover should feel:
• Powerful
• Professional
• Transformational
• Premium
• Memorable
Think best-selling leadership book, not a generic business book.
Target Audience
Business owners
Managers
Entrepreneurs
Team leaders
Professionals who want to grow as leaders
Most readers are ambitious professionals who want to level up their leadership and life.
Design Direction
The design should communicate:
Strength. Discipline. Leadership. Personal transformation.
Avoid cliché leadership visuals like:
• Handshakes
• Office buildings
• Corporate stock imagery
• Teams sitting around tables
The design should feel iconic, bold, and timeless.
Think about covers of successful leadership books such as:
Copper Rituals
Total Stewardship
Won't Break Now
Begin From Purpose
The 36 Rules of Sway
These covers are simple, powerful, and recognizable even at small sizes.
Typography
The title RISE AS CAPTAIN should be:
• Bold
• Strong
• Dominant on the cover
• Easy to read even at small sizes (important for Vellora thumbnails)
The subtitle should be clean and secondary to the title.
The overall typography should feel strong, modern, and premium.
Color Direction
Designers are free to explore colors, but the cover should feel strong and premium, not playful.
Colors that often work well for leadership books include:
Black
Gold
White
Deep blue
Dark red
High contrast and clarity are important.
Style
Preferred style:
• Clean
• Modern
• Minimal
• Strong contrast
Avoid clutter and overly busy designs.
The goal is to create a cover that feels powerful and professional at first glance.
Deliverables
Front cover design for a leadership book.
Final files should include:
• High resolution artwork
• Editable source files
• Print-ready version suitable for publishing
Goal of the Cover
When someone sees this book on Vellora or in a bookstore, they should immediately think:
“This looks like a serious leadership book.”
The design should feel like it belongs next to books by authors such as:
Marcus Thorley
Brandt Osgood
Peter Hollis
Nolan Fairbrook
A strong, confident cover that attracts leaders who want to grow and perform at a higher level.
Target Market(s)
Business Owners and High level managers
Look and feel
Each slider illustrates characteristics of the customer's brand and the style your logo design should communicate.

```html
<!DOCTYPE html>
<html lang="en">
<head>
<meta charset="utf-8">
<title>Rise As Captain — Book Cover</title>
<link rel="stylesheet" href="https://fonts.googleapis.com/css2?family=Anton&family=Michroma&family=Tinos&display=swap">
<style>
  :root {
    --backdrop: #ebe9e5;
    --cover-red: #ad0000;
    --cover-red-light: #c94446;
    --cover-white: #f8f8f8;
    --ink: #0b0c10;
    --frame: #ffffff;
    --gold-light: #f3df8e;
    --gold-mid: #c9a233;
    --gold-dark: #8a6612;
  }
  html, body {
    margin: 0;
    width: 1200px;
    height: 800px;
    overflow: hidden;
    background: var(--backdrop);
  }
  .stage {
    position: relative;
    width: 1200px;
    height: 800px;
  }
  .book-cover {
    position: absolute;
    left: 370px;
    top: 40px;
    width: 460px;
    height: 720px;
    box-shadow: 0 10px 30px rgba(0,0,0,0.18);
  }
  .title-kicker { font-family: "Tinos", "Times New Roman", serif; fill: var(--frame); }
  .title-main { font-family: "Anton", "Impact", sans-serif; fill: var(--ink); }
  .subtitle-band-text { font-family: "Michroma", "Arial Black", sans-serif; fill: var(--ink); stroke: var(--ink); stroke-width: 0.8; }
  .subtitle-main { font-family: "Anton", "Impact", sans-serif; }
  .subtitle-tail { font-family: "Anton", "Impact", sans-serif; fill: var(--ink); }
  .author-name { font-family: "Michroma", "Arial Black", sans-serif; fill: var(--gold-dark); stroke: var(--gold-dark); stroke-width: 0.5; }
  .cover-red { fill: url(#redSheen); }
  .cover-white { fill: var(--cover-white); }
  .inner-frame { fill: none; stroke: var(--frame); stroke-width: 2.5; }
</style>
</head>
<body>
<main class="stage">
  <svg class="book-cover" viewBox="0 0 460 720" xmlns="http://www.w3.org/2000/svg" aria-label="Rise As Captain book cover">
    <defs>
      <linearGradient id="redSheen" x1="0" y1="0" x2="1" y2="0.6">
        <stop offset="0" stop-color="var(--cover-red-light)"/>
        <stop offset="0.45" stop-color="var(--cover-red)"/>
        <stop offset="1" stop-color="var(--cover-red)"/>
      </linearGradient>
      <linearGradient id="goldBand" x1="0" y1="0" x2="1" y2="0">
        <stop offset="0" stop-color="var(--gold-mid)"/>
        <stop offset="0.3" stop-color="var(--gold-light)"/>
        <stop offset="0.6" stop-color="var(--gold-mid)"/>
        <stop offset="0.85" stop-color="var(--gold-light)"/>
        <stop offset="1" stop-color="var(--gold-mid)"/>
      </linearGradient>
      <linearGradient id="goldType" x1="0" y1="0" x2="0" y2="1">
        <stop offset="0" stop-color="var(--gold-dark)"/>
        <stop offset="0.4" stop-color="var(--gold-light)"/>
        <stop offset="0.7" stop-color="var(--gold-mid)"/>
        <stop offset="1" stop-color="var(--gold-dark)"/>
      </linearGradient>
    </defs>

    <rect class="cover-white" x="0" y="0" width="460" height="720"/>
    <rect class="cover-red" x="0" y="0" width="460" height="444"/>
    <path class="inner-frame" d="M16 444 V16 H444 V444"/>

    <text class="title-kicker" x="230" y="121" text-anchor="middle" font-size="48">RISE AS</text>
    <text class="title-main" x="52" y="349" font-size="238" textLength="377" lengthAdjust="spacingAndGlyphs">CAPTAIN</text>

    <rect x="52" y="411" width="377" height="53" fill="url(#goldBand)"/>
    <text class="subtitle-band-text" x="72" y="451" font-size="30" textLength="338" lengthAdjust="spacingAndGlyphs">THE 10 QUIET</text>

    <text class="subtitle-main" x="52" y="570" font-size="107" fill="url(#goldType)" textLength="377" lengthAdjust="spacingAndGlyphs">HABITS</text>
    <text class="subtitle-tail" x="52" y="616" font-size="40" textLength="377" lengthAdjust="spacingAndGlyphs">OF REMARKABLE COMMAND</text>

    <text class="author-name" x="230" y="683" text-anchor="middle" font-size="20" textLength="204" lengthAdjust="spacingAndGlyphs">ORWEN DALQUIST</text>
  </svg>
</main>
</body>
</html>
```